Crestway screen porch

Can you please design a flyer for me promoting my screen porch businessPlease remove the seamless gutters word from the title and add “screen porches” I have added the logo and a bunch of pictures from projects that I have done in the past. You can use words like Hillcrest Screen porches, etc

Target Market(s)

homeowners, contractors, builders

Industry/Entity Type

Construction

Requirements
Must have
• Dom Karsten
• Crestway Gutters
• 2957 Old Hwy 38 N, Greer, SC 29873
• 864-555-0186
Nice to have
• A few colors maybe 3 most
• nice looking font

```html
<!DOCTYPE html>
<html lang="en">
<head>
<meta charset="utf-8">
<title>Crestway Screen Porches Flyer</title>
<link href="https://fonts.googleapis.com/css2?family=Tinos:wght@400;700&display=swap" rel="stylesheet">
<style>
  :root{
    --stage:#2e2e2e;
    --photo-white:#f4f4f2;
    --ink-light:#ffffff;
  }
  html,body{margin:0;padding:0;width:1200px;height:1200px;overflow:hidden;background:var(--stage);}
  .canvas{position:relative;width:1200px;height:1200px;}
  .flyer{position:absolute;left:175px;top:50px;width:850px;height:1100px;overflow:hidden;
    font-family:"Tinos","Times New Roman",serif;color:var(--ink-light);}
  .flyer-art{position:absolute;inset:0;width:850px;height:1100px;}
  .brand{position:absolute;right:60px;top:70px;text-align:center;}
  .brand-name{margin:0;font-size:96px;font-weight:700;line-height:1;letter-spacing:1px;}
  .brand-tag{margin:6px 0 0;font-size:28px;font-weight:700;letter-spacing:5px;text-transform:uppercase;}
  .contact{position:absolute;right:40px;top:670px;width:300px;text-align:center;}
  .contact p{white-space:nowrap;}
  .contact-name{margin:0;font-size:36px;letter-spacing:3px;}
  .contact-company{margin:8px 0 0;font-size:33px;letter-spacing:1px;}
  .contact-phone{margin:12px 0 0;font-size:42px;font-weight:700;letter-spacing:3px;}
  .address{position:absolute;right:40px;top:960px;margin:0;font-size:20px;font-weight:700;letter-spacing:2px;white-space:nowrap;}
</style>
</head>
<body>
<div class="canvas">
  <section class="flyer">
    <svg class="flyer-art" viewBox="0 0 850 1100" xmlns="http://www.w3.org/2000/svg">
      <defs>
        <linearGradient id="roofGrad" x1="0" y1="0" x2="1" y2="1">
          <stop offset="0" stop-color="#4a5d76"/><stop offset="1" stop-color="#2c3b50"/>
        </linearGradient>
        <linearGradient id="woodGrad" x1="0" y1="0" x2="1" y2="1">
          <stop offset="0" stop-color="#5a3a2c"/><stop offset="1" stop-color="#2e1f1a"/>
        </linearGradient>
        <linearGradient id="stoneGrad" x1="0" y1="0" x2="0" y2="1">
          <stop offset="0" stop-color="#3a4654"/><stop offset="1" stop-color="#4a3a40"/>
        </linearGradient>
        <linearGradient id="porchGrad" x1="0" y1="0" x2="0" y2="1">
          <stop offset="0" stop-color="#e8e8e4"/><stop offset=".45" stop-color="#6c7075"/><stop offset="1" stop-color="#7d6a4c"/>
        </linearGradient>
        <linearGradient id="houseGrad" x1="0" y1="0" x2="0" y2="1">
          <stop offset="0" stop-color="#c6c5bb"/><stop offset=".6" stop-color="#8f9296"/><stop offset="1" stop-color="#6f5a45"/>
        </linearGradient>
        <linearGradient id="deckGrad" x1="0" y1="0" x2="0" y2="1">
          <stop offset="0" stop-color="#8e9da3"/><stop offset=".55" stop-color="#4d5a55"/><stop offset="1" stop-color="#c9ad78"/>
        </linearGradient>
      </defs>
      <rect x="0" y="0" width="850" height="1100" fill="url(#stoneGrad)" role="img" aria-label="Photo of stone and brick house wall"/>
      <polygon points="0,0 850,0 850,480 0,120" fill="url(#roofGrad)" role="img" aria-label="Photo of slate blue metal roof"/>
      <polygon points="540,380 850,330 850,1100 500,1100" fill="url(#woodGrad)" role="img" aria-label="Photo of dark wood siding"/>
      <polygon points="330,160 570,400 330,640 90,400" fill="var(--photo-white)"/>
      <polygon points="330,180 550,400 330,620 110,400" fill="url(#porchGrad)" role="img" aria-label="Photo of gabled screen porch on raised deck"/>
      <polygon points="640,220 850,430 640,640 430,430" fill="url(#houseGrad)" role="img" aria-label="Photo of white screen porch with stairs"/>
      <polygon points="130,560 300,730 130,900 -40,730" fill="#3f5a66" role="img" aria-label="Photo of trees reflected in window glass"/>
      <polygon points="320,610 500,790 320,970 140,790" fill="var(--photo-white)"/>
      <polygon points="320,628 482,790 320,952 158,790" fill="url(#deckGrad)" role="img" aria-label="Photo of screened deck interior with railing"/>
      <polygon points="200,880 340,1000 200,1100 60,1000" fill="#5b6a62" role="img" aria-label="Photo of screen porch corner with wooden floor"/>
    </svg>

    <header class="brand">
      <h1 class="brand-name">Crestway</h1>
      <p class="brand-tag">Screen Porches</p>
    </header>

    <div class="contact">
      <p class="contact-name">Dom Karsten</p>
      <p class="contact-company">Crestway Gutters</p>
      <p class="contact-phone">864-555-0186</p>
    </div>

    <p class="address">2957 Old Hwy 38 N, Greer, SC 29873</p>
  </section>
</div>
</body>
</html>
```